Business card design needed

New company based in Brisbane, Australia. Brindle Technologies. The business is focused on the delivery of network architecture design and deployment. We will provide both services and the sale of the necessary equipment to deliver the service. Cloud computing is an important element of our focus as this is an emerging market for enterprises in Queensland. Our target marketplace is medium to large corporations with complex infrastructure requirements. IT Management and above will be the typical entry point for us into these accounts. We would like to see the use of various shade of green, design should be clutter free and impress stability, trust and growth.
Updates
Hey Everyone
Just we let you all know we have changed this project to 'committed' payment status.
Looking forward to seeing the designs! Thanks for your efforts.
Best Regards
Martin
Industry/Entity Type
Architecture
Contact Information for Business Card
Brindle Technologies, Martin Coulter, Sales Director, Level 19 Harwell Court, 58 Kelvane Street, Brisbane QLD 4000, Ph +61 7 3946 2271, M +61 4 4208 6157, E martin.coulter@brindletechnologies-example.com.au
Look and feel
Each slider illustrates characteristics of the customer's brand and the style your logo design should communicate.

```html
<!DOCTYPE html>
<html lang="en">
<head>
<meta charset="utf-8">
<title>Brindle Technologies – Business Card</title>
<link rel="stylesheet" href="https://fonts.googleapis.com/css2?family=Mulish:wght@400;700;800&display=swap">
<style>
  :root {
    --lime-light: #99ff00;
    --lime-deep: #b0ff00;
    --ink: #0a0a0a;
    --name-white: #ffffff;
    --contact-ink: #111111;
  }
  html, body {
    margin: 0;
    padding: 0;
    overflow: hidden;
    background: #ffffff;
  }
  .business-card {
    position: relative;
    width: 1200px;
    height: 741px;
    overflow: hidden;
    background: linear-gradient(135deg, var(--lime-light) 0%, var(--lime-deep) 100%);
    font-family: "Mulish", "Century Gothic", sans-serif;
    color: var(--ink);
  }
  .company-name {
    position: absolute;
    left: 0;
    right: 0;
    top: 30px;
    margin: 0;
    text-align: center;
    font-weight: 800;
    font-size: 98px;
    letter-spacing: 0.5px;
    line-height: 1.1;
    color: var(--ink);
  }
  .contact-person {
    position: absolute;
    right: 59px;
    top: 272px;
    text-align: right;
    color: var(--name-white);
    font-weight: 800;
  }
  .contact-person .person-name {
    margin: 0;
    font-size: 57px;
    line-height: 1.1;
    letter-spacing: 1px;
  }
  .contact-person .person-role {
    margin: 4px 0 0;
    font-size: 38px;
    line-height: 1.1;
    letter-spacing: 0.5px;
  }
  .contact-details {
    position: absolute;
    left: 0;
    right: 0;
    top: 540px;
    text-align: center;
    font-weight: 400;
    font-size: 35px;
    line-height: 49px;
    color: var(--contact-ink);
  }
  .contact-details p { margin: 0; }
  .phone-line {
    display: flex;
    justify-content: center;
    gap: 88px;
  }
  .phone-item {
    display: inline-flex;
    align-items: center;
    gap: 2px;
  }
  .phone-icon {
    width: 28px;
    height: 30px;
    fill: var(--contact-ink);
  }
  .email { font-size: 33px; }
</style>
</head>
<body>
  <main class="business-card">
    <h1 class="company-name">Brindle Technologies</h1>

    <section class="contact-person">
      <p class="person-name">Martin Coulter</p>
      <p class="person-role">(Sales Director)</p>
    </section>

    <section class="contact-details">
      <p class="address">Level 19 Harwell Court, 58 Kelvane Street, Brisbane QLD 4000</p>
      <p class="phone-line">
        <span class="phone-item">
          <svg class="phone-icon" viewBox="0 0 24 24" aria-hidden="true">
            <path d="M6.6 10.8c1.4 2.8 3.8 5.1 6.6 6.6l2.2-2.2c.3-.3.7-.4 1-.2 1.1.4 2.3.6 3.6.6.6 0 1 .4 1 1V20c0 .6-.4 1-1 1C10.6 21 3 13.4 3 4c0-.6.4-1 1-1h3.5c.6 0 1 .4 1 1 0 1.3.2 2.5.6 3.6.1.3 0 .7-.2 1L6.6 10.8z"/>
          </svg>+61 7 3946 2271
        </span>
        <span class="phone-item">
          <svg class="phone-icon" viewBox="0 0 24 24" aria-hidden="true">
            <path d="M7 1.5h10c.8 0 1.5.7 1.5 1.5v18c0 .8-.7 1.5-1.5 1.5H7c-.8 0-1.5-.7-1.5-1.5V3c0-.8.7-1.5 1.5-1.5zm1 3v7h8v-7H8zm0 9v1.5h2V13.5H8zm3 0v1.5h2V13.5h-2zm3 0v1.5h2V13.5h-2zm-6 3v1.5h2v-1.5H8zm3 0v1.5h2v-1.5h-2zm3 0v1.5h2v-1.5h-2z"/>
          </svg>+61 4 4208 6157
        </span>
      </p>
      <p class="email">martin.coulter@brindletechnologies-example.com.au</p>
    </section>
  </main>
</body>
</html>
```